Business Card for Kinesiologist Practitioner

I need a logo and business card designing for a Kinesiologist Practitioner. I would like the card to be double sided. The look and feel of the logo and graphics should depict natural healing and well being. I would like a modern, fresh and contemporary design with a professional style. I have attached some logos and business cards that I liek from other natural health practitioners. I have also attached some logos that I like and a mock up of the business card style. Please however use your own creative input to change any element as you feel appropriate.

I have used the strap line "Quiet Meadow Care" which I would like underneath the logo. For the logo I like natural objects and possibly with 3 elements in the design as the course I have studied follows a "Lumora " healing concept (mind, body, soul). Maybe a tree or flower with 3 elements and a representation or suggestion of the human body somehow. You will see from the logos i have uploaded

Industry/Entity Type

Business

Contact Information for Business Card

Please see the mock up attached.

Font styles to use
Serif
Sans Serif

Colors
faa54b
acd036
fbee3d
85cae6

Requirements
Must have
• Note the colours are just suggested colours. Please us your own creative licence.

```html
<!DOCTYPE html>
<html lang="en">
<head>
<meta charset="utf-8">
<title>Quiet Meadow Care – Business Card</title>
<link href="https://fonts.googleapis.com/css2?family=Raleway:wght@300;400;500;800&display=swap" rel="stylesheet">
<style>
  :root {
    --leaf-green: #a6cd37;
    --ink: #1f2326;
    --paper: #ffffff;
    --backdrop: #e9ebe6;
  }
  * { box-sizing: border-box; margin: 0; padding: 0; }
  html, body {
    width: 1200px; height: 900px; overflow: hidden;
    background: var(--backdrop);
    font-family: "Raleway", sans-serif;
    color: var(--ink);
  }
  .canvas { position: relative; width: 1200px; height: 900px; }
  .card {
    position: absolute; left: 250px; width: 700px; height: 400px;
    background: var(--paper);
    box-shadow: 0 6px 18px rgba(0,0,0,0.12);
    overflow: hidden;
  }
  .card--front { top: 35px; }
  .card--back { top: 465px; }

  /* Front */
  .front-brand {
    position: absolute; left: 0; right: 0; top: 70px;
    display: flex; flex-direction: column; align-items: center;
  }
  .brand-mark {
    width: 110px; height: 110px; border-radius: 50%;
    background: var(--leaf-green);
    margin-bottom: 34px;
  }
  .brand-name {
    font-weight: 400; font-size: 27px; letter-spacing: 0.32em;
    text-transform: uppercase; padding-left: 0.32em; white-space: nowrap;
  }
  .brand-tagline { margin-top: 18px; font-size: 19px; font-weight: 400; }
  .brand-tagline .divider { color: var(--leaf-green); margin: 0 4px; }

  /* Back */
  .back-shape { position: absolute; inset: 0; }
  .back-brand {
    position: absolute; left: 20px; width: 220px; top: 145px;
    display: flex; flex-direction: column; align-items: center;
  }
  .back-brand .brand-mark { width: 66px; height: 66px; margin-bottom: 22px; }
  .back-brand .brand-name { font-size: 12px; letter-spacing: 0.22em; padding-left: 0.22em; }
  .practitioner { position: absolute; right: 34px; top: 48px; text-align: right; }
  .practitioner-name { font-size: 26px; line-height: 1; white-space: nowrap; }
  .practitioner-name strong { font-weight: 800; letter-spacing: 0.02em; }
  .practitioner-name .credentials { font-weight: 400; }
  .practitioner-role {
    margin-top: 6px; color: var(--paper); font-size: 15px;
    letter-spacing: 0.3em; font-weight: 400;
  }
  .contact-list {
    position: absolute; right: 30px; bottom: 60px; list-style: none;
    text-align: right;
  }
  .contact-item {
    display: flex; align-items: center; justify-content: flex-end;
    gap: 16px; font-size: 24px; font-weight: 400; line-height: 1.5;
    white-space: nowrap;
  }
  .contact-icon { width: 26px; height: 26px; flex: none; }
</style>
</head>
<body>
<main class="canvas">

  <section class="card card--front" aria-label="Card front">
    <div class="front-brand">
      <span class="brand-mark" aria-hidden="true"></span>
      <h1 class="brand-name">Quiet Meadow Care</h1>
      <p class="brand-tagline">mind<span class="divider">|</span>body<span class="divider">|</span>soul</p>
    </div>
  </section>

  <section class="card card--back" aria-label="Card back">
    <svg class="back-shape" viewBox="0 0 700 400" width="700" height="400" aria-hidden="true">
      <path d="M350 0 Q205 200 338 400" fill="none" stroke="var(--leaf-green)" stroke-width="6"/>
      <path d="M372 0 Q228 200 360 400 L700 400 L700 0 Z" fill="var(--leaf-green)"/>
    </svg>

    <div class="back-brand">
      <span class="brand-mark" aria-hidden="true"></span>
      <p class="brand-name">Quiet Meadow Care</p>
    </div>

    <div class="practitioner">
      <h2 class="practitioner-name"><strong>CLARA VENN</strong> <span class="credentials">dip. cert.</span></h2>
      <p class="practitioner-role">KINESIOLOGIST</p>
    </div>

    <ul class="contact-list">
      <li class="contact-item">
        <span>0400 123 456</span>
        <svg class="contact-icon" viewBox="0 0 26 26" aria-hidden="true">
          <circle cx="13" cy="13" r="11.5" fill="none" stroke="#fff" stroke-width="1.8"/>
          <path d="M9 7.5c-.8.4-1.5 1.4-1.2 2.8.6 2.9 4 6.6 7.2 7.6 1.4.4 2.4-.2 2.9-1l-2.2-1.9-1.3.9c-1.3-.6-3-2.4-3.5-3.7l1-1.2z" fill="#fff"/>
        </svg>
      </li>
      <li class="contact-item">
        <span>hello@quietmeadow.com</span>
        <svg class="contact-icon" viewBox="0 0 26 26" aria-hidden="true">
          <rect x="2" y="6" width="22" height="15" fill="none" stroke="#fff" stroke-width="1.8"/>
          <path d="M2 6l11 9 11-9M2 21l8-7M24 21l-8-7" fill="none" stroke="#fff" stroke-width="1.6"/>
        </svg>
      </li>
    </ul>
  </section>

</main>
</body>
</html>
```